Interior designer needs a product brochure design for a bedding collection

Hello designers,
My name is Mirelle, i need your professional services.
I am after a product brochure design for a bedding collection. (Please see attached bedding word document).
This collection will be sold in a black box with gold (foil) logo on the front.
I have attached a design of my business card for visual reference (matt black paper with black gloss A). As well as Danvers Pellt product marketing brochure which i love, in particular the way its layed out over several pages.
Personally, i feel this brochure will need to be layout out in a similar way otherwise it is too much information on one page.
Please use your creative license in regards to the size, shape, layout, materials used etc etc, but also be mindful of the overall costs. Having said that, i will be guided by you and will want to keep true to your vision also.
Thank you for your time and creativity
MirelleT

Target Market(s)

High end luxury market

Industry/Entity Type

Interior

Font styles to use
Other font styles liked:
• ebrima

Requirements
Must have
• logo
• information attached in word document including washing instructions
Nice to have
• Creative license
• I am told ebrima is the matching font, please let me know otherwise.
Should not have
• Over sized paper, i am fine with A4 and or smaller

```html
<!DOCTYPE html>
<html lang="en">
<head>
<meta charset="utf-8">
<title>MirelleT Bedding Brochure</title>
<link rel="stylesheet" href="https://fonts.googleapis.com/css2?family=Cutive&display=swap">
<style>
  :root {
    --backdrop: #3b3e41;
    --panel-brown: #231c1b;
    --panel-black: #120f10;
    --panel-white: #efeeeb;
    --gold: #b8975a;
    --gold-soft: #8e7448;
    --line-grey: #c9c6c0;
    --ink-grey: #6d6a66;
  }
  * { margin: 0; padding: 0; box-sizing: border-box; }
  html, body {
    width: 1200px; height: 900px; overflow: hidden;
    background: var(--backdrop);
  }
  .brochure {
    position: absolute; left: 90px; top: 130px;
    width: 1020px; height: 640px;
    display: flex;
    box-shadow: 0 18px 40px rgba(0,0,0,.35);
  }
  .panel {
    position: relative; width: 340px; height: 640px; overflow: hidden;
    font-family: "Cutive", "Courier New", serif;
    text-transform: uppercase;
  }
  .panel--philosophy { background: var(--panel-brown); color: var(--gold); }
  .panel--care { background: var(--panel-white); color: var(--ink-grey); }
  .panel--collection { background: var(--panel-black); color: var(--gold); }

  .diamond {
    position: absolute; left: 50%; top: 40px;
    width: 150px; height: 150px; margin-left: -75px;
  }
  .diamond__frame { position: absolute; inset: 0; }
  .diamond__content {
    position: absolute; inset: 0;
    display: flex; flex-direction: column; align-items: center; justify-content: center;
    text-align: center;
  }
  .brand {
    display: flex; align-items: center; justify-content: center; gap: 6px;
    font-size: 13px; letter-spacing: 1.5px; text-transform: none; color: var(--gold);
  }
  .brand__square { width: 7px; height: 7px; border: 1px solid currentColor; }

  .section-title {
    margin-top: 8px; font-size: 8px; font-weight: normal; letter-spacing: 3px;
  }
  .philosophy__body {
    position: absolute; top: 240px; left: 36px; right: 36px;
    font-size: 8px; line-height: 1.7; letter-spacing: .6px; text-align: center;
  }
  .philosophy__body p + p { margin-top: 12px; }

  .care__lines {
    margin-top: 8px; font-size: 6.5px; line-height: 1.8; letter-spacing: .8px;
    color: var(--gold-soft);
  }
  .care__note {
    position: absolute; top: 240px; left: 60px; right: 60px; text-align: center;
    font-size: 7px; line-height: 1.9; letter-spacing: .8px;
  }

  .collection__header {
    position: absolute; top: 50px; left: 0; right: 0; text-align: center;
  }
  .collection__kicker { font-size: 10px; letter-spacing: 2.5px; }
  .ornament {
    display: block; margin: 12px auto 0; width: 90px; height: 20px;
    background: linear-gradient(90deg, transparent, var(--gold-soft), transparent);
    opacity: .55;
  }
  .collection__title { margin-top: 12px; font-size: 11px; font-weight: normal; letter-spacing: 2.5px; }
  .collection__body {
    position: absolute; top: 160px; left: 40px; right: 40px; text-align: center;
    font-size: 8px; line-height: 1.7; letter-spacing: .6px;
  }
  .collection__photo {
    position: absolute; left: 0; right: 0; bottom: 0; height: 300px;
    background:
      radial-gradient(ellipse at 55% 60%, rgba(190,165,120,.5), transparent 60%),
      linear-gradient(180deg, var(--panel-black) 0%, #3a2f24 35%, #6b5a44 70%, #2a231c 100%);
  }
</style>
</head>
<body>
  <main class="brochure">
    <section class="panel panel--philosophy">
      <header class="diamond">
        <svg class="diamond__frame" viewBox="0 0 150 150" aria-hidden="true">
          <polygon points="75,1 149,75 75,149 1,75" fill="none" stroke="var(--gold-soft)" stroke-width="1"/>
        </svg>
        <div class="diamond__content">
          <div class="brand"><span class="brand__square"></span>MirelleT</div>
          <h2 class="section-title">Her Philosophy</h2>
        </div>
      </header>
      <div class="philosophy__body">
        <p>Ultimate design requires a constant pursuit of perfection. Taking the best that exists and making it better. Only if it doesn't exist, create it.</p>
        <p>Answering the perennial question of style versus function, MirelleT has fused the latest technology and style to create a bedding collection that is sumptuously smooth, silky and luxurious to the touch.</p>
        <p>She has used the finest available materials combined with a centuries-old manufacturing process to produce this exclusive 800 thread count collection made from 100% single-ply, long staple combed cotton, representing 3% of the world's highest-grade cotton production.</p>
      </div>
    </section>

    <section class="panel panel--care">
      <header class="diamond">
        <svg class="diamond__frame" viewBox="0 0 150 150" aria-hidden="true">
          <polygon points="75,1 149,75 75,149 1,75" fill="none" stroke="var(--line-grey)" stroke-width="1"/>
        </svg>
        <div class="diamond__content">
          <div class="brand"><span class="brand__square"></span>MirelleT</div>
          <div class="care__lines">
            <div>Bedding Collection</div>
            <div>Care and Washing</div>
            <div>Guide Enclosed</div>
          </div>
        </div>
      </header>
      <div class="care__note">
        <div>Wash cool with mild detergent.</div>
        <div>Line dry in shade.</div>
        <div>Warm iron.</div>
      </div>
    </section>

    <section class="panel panel--collection">
      <header class="collection__header">
        <div class="collection__kicker">Hotel Luxury Collection</div>
        <span class="ornament" role="img" aria-label="Gold flourish ornament"></span>
        <h1 class="collection__title">5 Star Luxury at Home</h1>
      </header>
      <p class="collection__body">MirelleT bedding collection in creamy white and penthouse grey is available in queen and king size duvet cover, fitted sheet, flat sheet, standard pillowcase, king standard pillowcase, tailored pillowcase and euro tailored pillowcase.</p>
      <div class="collection__photo" role="img" aria-label="Photograph of a luxurious bedroom with gold satin bedding, draped curtains and a checkered floor"></div>
    </section>
  </main>
</body>
</html>
```